Tallyleaf Web Design

Create Website Design for Tallyleaf. Tallyleaf is online application for collaboration team work system (task list management). More concept design for this project please find attach file ("tallyleaf website concept.pdf") . But my concept is just describe minimal features not bind design

For tallyleaf logo, i had already attach files. But i had not decided what color i chose, so it's okay if you suggest logo color for your suitable website design.
Updates

Dear All Designer,

I like brisk carousel (http://quorvanlabs.example/brisk-carousel/),
may be your concept design can adjust with this concept.
but don't worry about script for brisk carousel, my team will be handle
You just make website design to suitable with brisk carousel

but if you had own website design concept are welcome

thanks

Target Market(s)

Business Company

Industry/Entity Type

Management

```html
<!DOCTYPE html>
<html lang="en">
<head>
<meta charset="utf-8">
<title>Tallyleaf – Login</title>
<link rel="stylesheet" href="https://fonts.googleapis.com/css2?family=Source+Sans+3:wght@400;600;700&family=Nunito:wght@800&display=swap">
<style>
  :root {
    --page-bg: #ededed;
    --header-bg: #ffffff;
    --nav-text: #333333;
    --accent: #4ab3d1;
    --accent-dark: #1f6f86;
    --brand: #86bd22;
    --card-bg: #f7f7f7;
    --card-line: #dcdcdc;
    --field-bg: #ececec;
    --field-border: #c9c9c9;
    --muted-text: #555555;
    --footer-top: #1b6c7b;
    --footer-bottom: #0d4553;
    --footer-rule: #2d93a5;
    --footer-text: #e8f3f5;
    --social-blue: #4a76c2;
    --social-amber: #f2b01e;
  }
  * { box-sizing: border-box; margin: 0; padding: 0; }
  html, body { width: 1200px; height: 675px; overflow: hidden; }
  body { font-family: "Source Sans 3", sans-serif; background: var(--page-bg); }
  .canvas { position: relative; width: 1200px; height: 675px; overflow: hidden; background: var(--page-bg); }

  .site-header {
    position: absolute; left: 0; top: 0; width: 1200px; height: 85px;
    background: var(--header-bg); box-shadow: 0 1px 3px rgba(0,0,0,.18);
  }
  .brand-name {
    position: absolute; left: 146px; top: 14px;
    font-family: "Nunito", sans-serif; font-weight: 800; font-size: 50px;
    line-height: 56px; color: var(--brand); letter-spacing: -1px;
  }
  .main-nav { position: absolute; left: 535px; top: 32px; display: flex; align-items: center; gap: 17px; }
  .main-nav a { color: var(--nav-text); text-decoration: none; font-weight: 600; font-size: 17px; line-height: 24px; }
  .home-icon { width: 23px; height: 19px; margin-right: 1px; }
  .login-tab {
    position: absolute; left: 944px; top: 0; width: 112px; height: 85px;
    background: var(--accent); display: flex; align-items: center; justify-content: center; gap: 8px;
    color: #fff; font-weight: 600; font-size: 17px;
  }
  .login-tab .caret {
    width: 20px; height: 20px; border-radius: 50%; background: var(--accent-dark);
    display: flex; align-items: center; justify-content: center;
  }

  .login-stack { position: absolute; left: 466px; top: 168px; width: 272px; height: 260px; }
  .sheet {
    position: absolute; left: 6px; top: 8px; width: 258px; height: 240px;
    background: var(--card-bg); border: 1px solid var(--card-line);
    box-shadow: 0 1px 3px rgba(0,0,0,.12);
  }
  .sheet.back-a { transform: rotate(-1.6deg); }
  .sheet.back-b { transform: rotate(1.4deg) translate(2px, 4px); }
  .sheet.front {
    background: repeating-linear-gradient(90deg, #f8f8f8 0 2px, #f2f2f2 2px 4px);
  }
  .login-title {
    position: absolute; top: 57px; width: 100%; text-align: center;
    font-weight: 700; font-size: 12px; color: var(--muted-text);
  }
  .field {
    position: absolute; left: 27px; width: 198px; height: 24px;
    background: var(--field-bg); border: 1px solid var(--field-border); border-radius: 2px;
    box-shadow: inset 0 1px 2px rgba(0,0,0,.08);
    font-size: 9px; color: #333; padding-left: 8px; line-height: 22px;
  }
  .field.username { top: 89px; }
  .field.password { top: 122px; }
  .login-button {
    position: absolute; left: 92px; top: 172px; width: 73px; height: 25px;
    border-radius: 13px; border: 1px solid #bdbdbd;
    background: linear-gradient(#fbfbfb, #dedede);
    box-shadow: 0 2px 2px rgba(0,0,0,.2);
    font-size: 10px; color: #333; text-align: center; line-height: 23px;
  }

  .site-footer {
    position: absolute; left: 0; top: 532px; width: 1200px; height: 143px;
    border-top: 2px solid var(--footer-rule);
    background: linear-gradient(var(--footer-top), var(--footer-bottom));
    color: var(--footer-text);
  }
  .footer-nav { position: absolute; left: 136px; top: 24px; display: flex; gap: 15px; }
  .footer-nav a, .footer-note { color: var(--footer-text); text-decoration: none; font-weight: 600; font-size: 15px; line-height: 21px; }
  .footer-note { position: absolute; left: 136px; }
  .footer-note.copyright { top: 45px; }
  .footer-note.terms { top: 66px; }
  .follow { position: absolute; left: 878px; top: 27px; display: flex; align-items: center; gap: 8px; font-weight: 600; font-size: 15px; }
  .follow-label { margin-right: 4px; }
  .social { width: 31px; height: 30px; border-radius: 4px; }
  .social.network-a { background: var(--social-blue); }
  .social.network-b { background: var(--social-amber); }
</style>
</head>
<body>
<div class="canvas">
  <header class="site-header">
    <div class="brand-name">tallyleaf</div>
    <nav class="main-nav">
      <svg class="home-icon" viewBox="0 0 23 19" aria-label="Home">
        <path d="M11.5 1 L1 10 H4 V18 H9.5 V12.5 H13.5 V18 H19 V10 H22 Z" fill="#4ab3d1"/>
      </svg>
      <a href="#">About Us</a>
      <a href="#">Products</a>
      <a href="#">Solutions</a>
      <a href="#">Contact Us</a>
    </nav>
    <div class="login-tab">
      <span>Login</span>
      <span class="caret"><svg width="8" height="6" viewBox="0 0 8 6"><path d="M0 0 H8 L4 6 Z" fill="#fff"/></svg></span>
    </div>
  </header>

  <main class="login-stack">
    <div class="sheet back-a"></div>
    <div class="sheet back-b"></div>
    <div class="sheet front">
      <div class="login-title">Please Login here...</div>
      <div class="field username">Username</div>
      <div class="field password">Password</div>
      <div class="login-button">Login</div>
    </div>
  </main>

  <footer class="site-footer">
    <nav class="footer-nav">
      <a href="#">Home</a>
      <a href="#">About Us</a>
      <a href="#">Products</a>
      <a href="#">Solutions</a>
      <a href="#">Contact Us</a>
    </nav>
    <div class="footer-note copyright">Copyright@2013, tallyleaf</div>
    <div class="footer-note terms">Terms &amp; Privacy Policy</div>
    <div class="follow">
      <span class="follow-label">Follow Us :</span>
      <span class="social network-a" role="img" aria-label="Social network link"></span>
      <span class="social network-b" role="img" aria-label="News feed link"></span>
    </div>
  </footer>
</div>
</body>
</html>
```